GIFT BOX FOR DECORATION CHRISTMAS

Good evening, the job to do is to create a gift box with the attached path.
The Gift Box is for a company that deals with personalized Christmas decorations.
The graphics must be "very clean", the colors to be used are RED and GREEN the colors of Christmas. In the graphics we put a beautiful bow and the company logo.
I am attaching the company's logo to some examples.

good job

Target Market(s)

Being a Gift Box for a Christmas product must be suitable for everyone.

Font styles to use
Sans Serif

Colors
00a990
ec1f27

Requirements
Must have
• The project must have a background (green / red) a bow, inside the logo must be placed. In the sides of the Gift, reverse the color (as per the sample from last year attached) insert the PALWIRE logo and PIXORVA + WEB SITE (www.casaluminara.it)

```html
<!DOCTYPE html>
<html lang="en">
<head>
<meta charset="utf-8">
<title>Gift Box Dieline – Casa Luminara</title>
<link rel="stylesheet" href="https://fonts.googleapis.com/css2?family=Cormorant+Garamond:wght@500&display=swap">
<style>
  :root {
    --green: #00a990;
    --red: #ec1f27;
    --white: #ffffff;
    --page: #ffffff;
    --navy: #2e3a8c;
  }
  html, body {
    margin: 0;
    padding: 0;
    width: 1200px;
    height: 1200px;
    overflow: hidden;
    background: var(--page);
  }
  .dieline { display: block; width: 1200px; height: 1200px; }
  .green { fill: var(--green); }
  .red { fill: var(--red); }
  .white { fill: var(--white); }
  .label {
    font-family: "Cormorant Garamond", Georgia, serif;
    font-weight: 500;
    fill: var(--white);
  }
  .greeting { font-size: 16.5px; letter-spacing: 0.3px; }
  .brand-name { font-size: 15px; }
  .side-label { font-size: 7.5px; fill: var(--white); }
  .web-address { font-size: 6px; fill: var(--white); letter-spacing: 0.2px; }
  .social-dot { fill: var(--navy); }
</style>
</head>
<body>
<svg class="dieline" viewBox="0 0 1000 1000" xmlns="http://www.w3.org/2000/svg">

  <!-- Front face -->
  <g class="front-face">
    <path class="red" d="M222 250 V225 Q222 213 234 213 H346 Q358 213 358 225 V250 Z"/>
    <rect class="green" x="162" y="249" width="255" height="99"/>
    <rect class="white" x="211" y="293" width="158" height="10" rx="5"/>
    <rect class="red" x="162" y="347" width="255" height="297" role="img" aria-label="Red gift wrap with white polka dots"/>
    <rect class="green" x="268" y="347" width="44" height="297"/>
    <rect class="green" x="162" y="478" width="255" height="42"/>
    <circle class="green" cx="290" cy="500" r="78"/>
    <text class="label brand-name" x="290" y="478" text-anchor="middle">Casa Luminara</text>
    <text class="label greeting" x="290" y="531" text-anchor="middle">MERRY</text>
    <text class="label greeting" x="290" y="554" text-anchor="middle">CHRISTMAS</text>
    <path class="green" d="M133 367 L162 350 V645 H157 L133 620 Z"/>
    <path class="green" d="M162 643 H417 L410 660 L415 722 H401 L370 693 H290 V705 L255 722 H170 L165 660 Z"/>
  </g>

  <!-- Left side panel -->
  <g class="side-panel">
    <path class="green" d="M424 307 H510 V350 H517 V645 L510 650 L466 693 H433 L420 650 L424 645 Z"/>
    <circle class="social-dot" cx="438" cy="561" r="7"/>
    <text class="label side-label" x="448" y="564">PALWIRE</text>
    <rect class="social-dot" x="431" y="578" width="14" height="14" rx="3"/>
    <text class="label side-label" x="448" y="588">PIXORVA</text>
    <text class="label web-address" x="429" y="609">www.casaluminara.it</text>
  </g>

  <!-- Back face -->
  <g class="back-face">
    <path class="red" d="M517 255 V227 Q517 214 530 214 H755 Q768 214 768 227 V255 Z"/>
    <rect class="green" x="515" y="253" width="256" height="95"/>
    <rect class="red" x="515" y="347" width="256" height="297" role="img" aria-label="Red gift wrap with white polka dots"/>
    <rect class="white" x="614" y="322" width="59" height="58" rx="8"/>
    <path class="green" d="M517 643 H772 L765 660 L770 722 H756 L725 693 H643 V705 L608 722 H523 L520 660 Z"/>
  </g>

  <!-- Right side panel -->
  <g class="side-panel">
    <path class="green" d="M777 307 H862 V350 H866 V645 L820 693 H787 L775 645 Z"/>
  </g>
</svg>
</body>
</html>
```